Brisk Venture - Logo & Business Card

I have briefly designed a logo for my small events business and need it fixed up. I would prefer it to be white on black background. I also need a PDF for business cards, I would like them to be black with the logo on one side and my details on the other side:

Brisk Venture
Corinna-May Feltwell
Founder / Director
0471 820 237
corinna@briskventure.com.au

```html
<!DOCTYPE html>
<html lang="en">
<head>
<meta charset="utf-8">
<title>Brisk Venture – Business Card</title>
<link rel="stylesheet" href="https://fonts.googleapis.com/css2?family=Arimo:wght@400;700&family=Lobster+Two:ital,wght@1,700&display=swap">
<style>
  :root {
    --backdrop: #9c5a36;
    --card-black: #000000;
    --card-white: #ffffff;
    --aqua: #a3dcdf;
    --teal-ink: #3fb8ad;
    --text-dark: #111111;
    --text-light: #ffffff;
  }
  * { margin: 0; padding: 0; box-sizing: border-box; }
  html, body {
    width: 1200px; height: 914px; overflow: hidden;
    background: var(--backdrop);
  }
  .stage { position: relative; width: 1200px; height: 914px; }

  .card {
    position: absolute;
    box-shadow: 0 10px 28px rgba(0,0,0,0.35);
  }
  .card svg.card-shapes { position: absolute; inset: 0; display: block; }

  /* Logo side */
  .card--logo {
    left: 560px; top: 60px; width: 580px; height: 331px;
    background: var(--card-white);
  }
  .card--logo .brand {
    position: absolute; left: 90px; top: 130px;
  }

  .brand {
    display: flex; align-items: center; gap: 12px;
    font-family: "Arimo", Arial, sans-serif;
    font-weight: 700;
    color: var(--teal-ink);
    font-size: 30px;
    letter-spacing: 0.5px;
  }
  .brand__dot {
    width: 30px; height: 30px; border-radius: 50%;
    background: var(--teal-ink);
  }

  /* Details side */
  .card--details {
    left: 60px; top: 430px; width: 720px; height: 411px;
    background: var(--card-black);
  }
  .holder-name {
    position: absolute; left: 40px; top: 40px;
    font-family: "Lobster Two", Georgia, serif;
    font-style: italic; font-weight: 700;
    font-size: 40px; color: var(--aqua);
    letter-spacing: 1px;
  }
  .holder-role {
    position: absolute; left: 42px; top: 94px;
    font-family: "Arimo", Arial, sans-serif;
    font-size: 15px; color: var(--text-light);
  }
  .contact-list {
    position: absolute; left: 36px; top: 220px;
    list-style: none;
    font-family: "Arimo", Arial, sans-serif;
    font-size: 19px; color: var(--text-dark);
  }
  .contact-list li {
    display: flex; align-items: center; gap: 14px;
    margin-bottom: 14px;
  }
  .contact-list svg { width: 18px; height: 14px; flex: none; }
  .card--details .brand {
    position: absolute; left: 530px; top: 300px;
    font-size: 22px; gap: 9px;
  }
  .card--details .brand__dot { width: 22px; height: 22px; }
</style>
</head>
<body>
<main class="stage">

  <section class="card card--logo" aria-label="Business card, logo side">
    <div class="brand">
      <span class="brand__dot"></span>
      <span class="brand__name">Brisk Venture</span>
    </div>
  </section>

  <section class="card card--details" aria-label="Business card, details side">
    <svg class="card-shapes" width="720" height="411" viewBox="0 0 720 411" aria-hidden="true">
      <rect width="720" height="411" fill="var(--card-black)"/>
      <polygon points="0,135 458,210 505,385 0,385" fill="var(--aqua)"/>
      <polygon points="478,213 720,253 720,385 524,385" fill="var(--card-white)"/>
    </svg>

    <h1 class="holder-name">Corinna-May Feltwell</h1>
    <p class="holder-role">Founder / Director</p>

    <ul class="contact-list">
      <li>
        <svg viewBox="0 0 18 14" aria-hidden="true">
          <path d="M1 4 Q9 -1 17 4 L15 6 L12 5 L12 3 Q9 2 6 3 L6 5 L3 6 Z" fill="var(--text-dark)"/>
          <rect x="4" y="7" width="10" height="6" rx="1" fill="var(--text-dark)"/>
        </svg>
        <span>0471 820 237</span>
      </li>
      <li>
        <svg viewBox="0 0 18 14" aria-hidden="true">
          <rect x="1" y="1.5" width="16" height="11" fill="var(--text-dark)"/>
          <path d="M1.5 2 L9 8 L16.5 2" stroke="var(--aqua)" stroke-width="1.4" fill="none"/>
        </svg>
        <span>corinna@briskventure.com.au</span>
      </li>
    </ul>

    <div class="brand">
      <span class="brand__dot"></span>
      <span class="brand__name">Brisk Venture</span>
    </div>
  </section>

</main>
</body>
</html>
```